Brochure Design Project

Looking for 8.5 x 5.5 brochure for new indoor cycling studio. This will be the first upscale, boutique indoor cycling studio in our area. Our studio will be decorated in modern grays and whites with pops of orange and blue. Looking to incorporate the image of oranges in clear cylinders on the front, and then it exploding on the back. Open to other ideas. Looking for modern and fresh.
Logo attached. Copy below.
"Are you ready to Velmo? Bring It."
"Velmo Indoor Cycling Studio is a state of the art boutique cycling studio located in the Harlow Sports Center in Ashby Meadows.
The Studio offers cycling fitness programs for everyone from beginners to seasoned indoor cyclists. By incorporating best in class bikes, technology and facilities, Velmo Indoor Cycling Studio sets the standard in indoor cycling."
"What we Bring:
-State of the art online reservation system
-Top of the Line Bikes that are specially tuned for optimum performance
-Stadium Seating. Premium Sound. Smart Lighting.
-High energy certified instructors
-The best customer service....Period."
"Come take a Velmo!"
2281 Penwick Lane
Brentwood, TN 37027
615.555.0192
velmospin.example

```html
<!DOCTYPE html>
<html lang="en">
<head>
<meta charset="utf-8">
<title>Velmo Indoor Cycling Studio – What We Bring</title>
<link rel="stylesheet" href="https://fonts.googleapis.com/css2?family=Bebas+Neue&family=Oswald:wght@500&display=swap">
<style>
  :root {
    --paper: #ffffff;
    --title-gray: #7b7b7b;
    --ring-gray: #b9bbbc;
    --ring-edge: #999b9c;
    --accent-orange: #ff3d1f;
    --accent-blue: #3db7ee;
    --tire-black: #0d0d0d;
  }
  * { margin: 0; padding: 0; box-sizing: border-box; }
  html, body { width: 776px; height: 1200px; overflow: hidden; background: var(--paper); }
  .panel {
    position: relative;
    width: 776px;
    height: 1200px;
    overflow: hidden;
    background: var(--paper);
    font-family: "Bebas Neue", "Oswald", sans-serif;
  }
  .decor { position: absolute; inset: 0; }
  .benefits {
    position: absolute;
    left: 194px;
    top: 342px;
    width: 500px;
    list-style: none;
    color: var(--accent-blue);
    font-size: 36px;
    line-height: 43px;
    white-space: nowrap;
  }
  .benefits li {
    position: relative;
    padding-left: 11px;
    margin-bottom: 11px;
  }
  .benefits li::before {
    content: "";
    position: absolute;
    left: 0;
    top: 10px;
    width: 5px;
    height: 22px;
    background: var(--accent-orange);
  }
  .contact {
    position: absolute;
    left: 11px;
    top: 1164px;
    color: var(--accent-blue);
    font-family: "Oswald", "Bebas Neue", sans-serif;
    font-weight: 500;
    font-size: 15px;
    line-height: 20px;
    white-space: nowrap;
  }
</style>
</head>
<body>
<main class="panel">
  <svg class="decor" width="776" height="1200" viewBox="0 0 776 1200">
    <!-- main frame ring -->
    <circle cx="393" cy="548" r="327" fill="none" stroke="var(--ring-gray)" stroke-width="40"/>
    <circle cx="393" cy="548" r="347" fill="none" stroke="var(--ring-edge)" stroke-width="2"/>
    <circle cx="393" cy="548" r="307" fill="none" stroke="var(--ring-edge)" stroke-width="4"/>

    <!-- side rings -->
    <circle cx="72" cy="309" r="40" fill="none" stroke="var(--ring-gray)" stroke-width="10"/>
    <circle cx="72" cy="309" r="45" fill="none" stroke="var(--ring-edge)" stroke-width="1.5"/>

    <circle cx="-28" cy="404" r="70" fill="none" stroke="var(--ring-gray)" stroke-width="30"/>
    <circle cx="-28" cy="404" r="85" fill="none" stroke="var(--ring-edge)" stroke-width="2"/>

    <circle cx="792" cy="658" r="42" fill="none" stroke="var(--ring-gray)" stroke-width="10"/>
    <circle cx="792" cy="658" r="47" fill="none" stroke="var(--ring-edge)" stroke-width="1.5"/>

    <circle cx="785" cy="837" r="108" fill="none" stroke="var(--ring-gray)" stroke-width="20"/>
    <circle cx="785" cy="837" r="118" fill="none" stroke="var(--ring-edge)" stroke-width="2"/>
    <circle cx="785" cy="837" r="98" fill="none" stroke="var(--ring-edge)" stroke-width="3"/>

    <!-- accent dots -->
    <circle class="dot-solid" cx="656" cy="75" r="23" fill="var(--accent-orange)"/>
    <circle class="dot-ring" cx="591" cy="97" r="13" fill="none" stroke="var(--accent-orange)" stroke-width="7"/>

    <!-- heading sits above the rings -->
    <text class="heading" x="54" y="246" textLength="666" lengthAdjust="spacingAndGlyphs"
          font-family="'Bebas Neue', sans-serif" font-size="158" fill="var(--title-gray)">WHAT WE BRING</text>

    <!-- wheel artwork area -->
    <defs>
      <radialGradient id="wheel-fill" cx="50%" cy="50%" r="50%">
        <stop offset="0%" stop-color="#f4f4f4"/>
        <stop offset="84%" stop-color="#e2e2e2"/>
        <stop offset="88%" stop-color="#1a1a1a"/>
        <stop offset="100%" stop-color="var(--tire-black)"/>
      </radialGradient>
    </defs>
    <circle class="wheel-art" cx="666" cy="1106" r="198" fill="url(#wheel-fill)"
            role="img" aria-label="Bicycle wheel with spokes"/>
  </svg>

  <ul class="benefits">
    <li>State of the art online<br>reservation system</li>
    <li>Top of the line bikes that are<br>specially tuned for optimum<br>performance</li>
    <li>Stadium seating. Premium sound.<br>Smart lighting</li>
    <li>High energy certified instructors</li>
    <li>The best customer service</li>
  </ul>

  <p class="contact">2281 Penwick Lane Brentwood, TN 37027 &nbsp;|&nbsp; 615.555.0192 &nbsp;|&nbsp; www.velmospin.example</p>
</main>
</body>
</html>
```